A5 5mm Grid and Dot Grid Page Layout

I need 2 designs:
1] A5 (5.75" x 8" inches final trimmed page size ) 128 journal pages with a 5mm x 5mm grid layout
2} A5 (5.75" x 8" inches final trimmed page size) 128 journal pages with 5mm x 5mm dot grid layout
First and last page should be blank
grid and dot grid should be a light gray color
Final design should you in PDF format

Target Market(s)

Fountain Pen Notebooks

Industry/Entity Type

Notebooks and Journals

Colors

Designer to choose only greyscale colors for use in the design.

Requirements
Must have
• Light gray 5mm x 5mm grid and dot grid page layout. Very thin lines
Should not have
• Thick black grid or dots

```html
<!DOCTYPE html>
<html lang="en">
<head>
<meta charset="utf-8">
<title>A5 5mm Grid and Dot Grid Journal Pages</title>
<link rel="stylesheet" href="https://fonts.googleapis.com/css2?family=Inter:wght@400&display=swap">
<style>
  :root {
    --backdrop: #c4c2c3;
    --paper: #ffffff;
    --grid-line: #dcdcdc;
    --grid-frame: #d2d2d2;
    --dot: #a9a9a9;
  }
  html, body {
    margin: 0;
    padding: 0;
    overflow: hidden;
    font-family: "Inter", sans-serif;
  }
  .spread {
    position: relative;
    width: 1200px;
    height: 840px;
    background: var(--backdrop);
    overflow: hidden;
  }
  .page {
    position: absolute;
    top: 18px;
    width: 568px;
    height: 805px;
    background: var(--paper);
  }
  .page--grid { left: 14px; }
  .page--dots { left: 613px; }
  .page svg {
    display: block;
    width: 568px;
    height: 805px;
  }
  .grid-line { stroke: var(--grid-line); stroke-width: 0.8; fill: none; }
  .grid-frame { stroke: var(--grid-frame); stroke-width: 1; fill: none; }
  .grid-dot { fill: var(--dot); }
</style>
</head>
<body>
  <main class="spread">
    <section class="page page--grid" aria-label="5mm square grid page">
      <svg viewBox="0 0 568 805" xmlns="http://www.w3.org/2000/svg">
        <defs>
          <pattern id="square-grid" x="7" y="7" width="19.2" height="19.2" patternUnits="userSpaceOnUse">
            <path class="grid-line" d="M19.2 0 V19.2 M0 19.2 H19.2"/>
          </pattern>
        </defs>
        <rect x="7" y="7" width="556.8" height="787.2" fill="url(#square-grid)"/>
        <rect class="grid-frame" x="7" y="7" width="556.8" height="787.2"/>
      </svg>
    </section>

    <section class="page page--dots" aria-label="5mm dot grid page">
      <svg viewBox="0 0 568 805" xmlns="http://www.w3.org/2000/svg">
        <defs>
          <pattern id="dot-grid" x="-2.4" y="4.6" width="19.2" height="19.2" patternUnits="userSpaceOnUse">
            <circle class="grid-dot" cx="9.6" cy="2.4" r="0.9"/>
          </pattern>
        </defs>
        <rect x="0" y="4" width="568" height="795" fill="url(#dot-grid)"/>
      </svg>
    </section>
  </main>
</body>
</html>
```